Leadership Brenvale Brochure Design*

We host a local leadership development program every two years. We need a brochure to promote the program. We would like it to be 8 1/2 x 11, tri-fold. I have attached a Word document with the necessary info for the brochure. The brochure will be professionally printed. We would like the final design to be in InDesign.

Target Market(s)

Potential participants of our leadership program. They will be local leaders, male and female, from 30-60 years of age.

Requirements
Must have
• Content as detailed in the Word document attached. Our logo.
Nice to have
• A design that is attractive to young professionals.

```html
<!DOCTYPE html>
<html lang="en">
<head>
<meta charset="utf-8">
<title>Leadership Brenvale – Schedule</title>
<link rel="stylesheet" href="https://fonts.googleapis.com/css2?family=Hind:wght@400;500;600&family=Saira+Condensed:wght@800&display=swap">
<style>
  :root{
    --teal-light:#6cc4c3;
    --teal-pale:#a6dcdc;
    --teal-deep:#2a7f99;
    --navy-text:#0d5b78;
    --panel:#0a5570;
    --panel-dark:#073f55;
    --band:#053449;
    --tab:#567b88;
    --mint:#7fd8cf;
    --white:#ffffff;
    --ink:#111;
  }
  *{margin:0;padding:0;box-sizing:border-box}
  html,body{width:1200px;height:927px;overflow:hidden;background:#fff}
  body{font-family:"Hind",Arial,sans-serif;position:relative}

  /* ---------- overview panel ---------- */
  .overview{position:absolute;left:0;top:0;width:400px;height:927px;background:var(--white);overflow:hidden}
  .overview__art-top{position:absolute;left:0;top:0;width:400px;height:120px;
    background:linear-gradient(180deg,var(--teal-light) 0%,var(--teal-pale) 55%,var(--white) 100%)}
  .overview__art-bottom{position:absolute;left:0;top:540px;width:400px;height:387px;
    background:linear-gradient(180deg,var(--white) 0%,var(--teal-pale) 14%,var(--teal-light) 40%,var(--teal-deep) 88%,var(--panel) 100%)}
  .overview__heading{position:absolute;left:42px;top:152px;font-size:21px;font-weight:600;color:var(--navy-text)}
  .overview__body{position:absolute;left:42px;top:194px;width:320px;font-size:12.2px;line-height:14.5px;color:var(--ink)}
  .overview__body p + p{margin-top:14.5px}
  .goals{position:absolute;left:47px;top:336px;width:320px;border-left:1.5px solid var(--teal-pale);padding-left:10px;list-style:none}
  .goals li{font-size:15.6px;line-height:18.2px;color:var(--navy-text);margin-bottom:18px}
  .goals li:last-child{margin-bottom:0}

  /* ---------- schedule panel ---------- */
  .schedule{position:absolute;left:400px;top:0;width:800px;height:927px;background:var(--panel);overflow:hidden}
  .schedule__band{position:absolute;left:0;width:800px;background:var(--band)}
  .schedule__band--top{top:0;height:51px}
  .schedule__band--bottom{top:878px;height:49px}
  .schedule__title{position:absolute;left:24px;top:66px;font-family:"Saira Condensed",Impact,sans-serif;font-weight:800;font-size:70px;letter-spacing:-0.5px;line-height:1;color:var(--white)}

  .session{position:absolute}
  .session__head{display:flex}
  .session__date{width:50px;background:var(--tab);color:var(--white);font-weight:600;font-size:19px;letter-spacing:.3px;
    writing-mode:vertical-rl;transform:rotate(180deg);display:flex;align-items:center;justify-content:center;line-height:1}
  .session__info{background:var(--panel-dark);color:var(--white);font-size:17.5px;font-weight:500;line-height:26px;
    display:flex;flex-direction:column;justify-content:flex-end;padding:0 0 4px 10px;white-space:nowrap}
  .session__items{list-style:none;margin-top:-1px;padding-left:60px}
  .session__items li{color:var(--mint);font-size:15.8px;font-weight:500;line-height:26px;position:relative;padding-left:9px;white-space:nowrap}
  .session__items li::before{content:"·";position:absolute;left:0}
</style>
</head>
<body>

<section class="overview">
  <div class="overview__art-top" role="img" aria-label="Decorative teal wave swooshes"></div>
  <h2 class="overview__heading">Program Overview</h2>
  <div class="overview__body">
    <p>Leadership Brenvale is a leadership certification program designed to prepare the leaders of tomorrow. During the five-month program, participants get an in-depth view of community issues, develop leadership skills necessary to assume leadership roles, and are exposed to community involvement opportunities.</p>
    <p>Leadership Brenvale will provide participants<br>with the opportunities to:</p>
  </div>
  <ul class="goals">
    <li>Build and demonstrate leadership an communication skills</li>
    <li>Think critically about key business, policy, and civic issues facing Brenvale County</li>
    <li>Build meaningful, long-lasting connections</li>
    <li>Establish ongoing dialogues with experience community leaders</li>
  </ul>
  <div class="overview__art-bottom" role="img" aria-label="Illustration of a speaker at a podium facing a large audience beneath teal wave swooshes"></div>
</section>

<section class="schedule">
  <div class="schedule__band schedule__band--top" role="img" aria-label="Decorative diagonal stripe band"></div>
  <div class="schedule__band schedule__band--bottom" role="img" aria-label="Decorative diagonal stripe band"></div>

  <h1 class="schedule__title">SCHEDULE</h1>

  <article class="session" style="left:0;top:154px">
    <div class="session__head">
      <div class="session__date">JAN 17</div>
      <div class="session__info" style="width:296px;height:88px">
        <span>Organizational Retreat &amp; Dinner</span>
        <span>(Attendance Mandatory)</span>
        <span>10:00 a.m. – 7:00 p.m.</span>
      </div>
    </div>
    <ul class="session__items">
      <li>Introductions</li><li>Team Building</li><li>Motivation</li><li>Leadership Styles</li><li>Social Hour/Dinner</li>
    </ul>
  </article>

  <article class="session" style="left:0;top:398px">
    <div class="session__head">
      <div class="session__date">JAN 31</div>
      <div class="session__info" style="width:300px;height:73px">
        <span>Business &amp; Industry</span>
        <span>8:30 a.m. – 4:00 p.m.</span>
      </div>
    </div>
    <ul class="session__items">
      <li>Business &amp; Industry Panel</li><li>Tour of Ferrodyne Manufacturing facility</li><li>Tour of Aldridge Tool Company</li><li>“Taking your vision into B&amp;I”</li>
    </ul>
  </article>

  <article class="session" style="left:0;top:608px">
    <div class="session__head">
      <div class="session__date">FEB 21</div>
      <div class="session__info" style="width:300px;height:73px">
        <span>Education</span>
        <span>8:30 a.m. – 4:00 p.m.</span>
      </div>
    </div>
    <ul class="session__items">
      <li>Tour of selected programs at BCC</li><li>College Career Program overview</li><li>Lunch at Brenvale Career and<br>College Academy</li><li>Tour of BCCA</li><li>Overview of CTE program paths</li>
    </ul>
  </article>

  <article class="session" style="left:400px;top:115px">
    <div class="session__head">
      <div class="session__date">MAR 14</div>
      <div class="session__info" style="width:299px;height:73px;padding-left:4px">
        <span>Future Technologies &amp; Communications</span>
        <span>8:30 a.m. – 4:00 p.m.</span>
      </div>
    </div>
    <ul class="session__items" style="padding-left:54px">
      <li>BCC Presents interview</li><li>Trends and forecasts</li><li>Marketing &amp; communications panel</li>
    </ul>
  </article>

  <article class="session" style="left:400px;top:270px">
    <div class="session__head">
      <div class="session__date">APR 04</div>
      <div class="session__info" style="width:299px;height:73px;padding-left:4px">
        <span>Government</span>
        <span>8:30 a.m. – 4:00 p.m.</span>
      </div>
    </div>
    <ul class="session__items" style="padding-left:54px">
      <li>Overview of state/federal government</li><li>Overview of city/county government</li><li>Tour of Harlow Ridge Correctional Institute</li><li>Tour of courthouse</li><li>Judicial presentations</li>
    </ul>
  </article>

  <article class="session" style="left:400px;top:480px">
    <div class="session__head">
      <div class="session__date">MAY 02</div>
      <div class="session__info" style="width:299px;height:73px;padding-left:4px">
        <span>Health &amp; Wellness</span>
        <span>8:30 a.m. – 4:00 p.m.</span>
      </div>
    </div>
    <ul class="session__items" style="padding-left:54px">
      <li>Tour of Lower Weston Hospice</li><li>Community Wellness Roundtable</li><li>Tour of Marrow Cancer Care Center</li><li>Virtual Medicine Tutorial</li><li>Tour of BRHS</li>
    </ul>
  </article>

  <article class="session" style="left:400px;top:687px">
    <div class="session__head">
      <div class="session__date">MAY 18</div>
      <div class="session__info" style="width:302px;height:74px;padding-left:4px">
        <span>Graduation Ceremony and Luncheon</span>
        <span>(12:00 p.m.)</span>
      </div>
    </div>
    <ul class="session__items" style="padding-left:54px">
      <li>Participants are encouraged to invite<br>their employer/supervisor/mentor/<br>special guest (x2)</li>
    </ul>
  </article>
</section>

</body>
</html>
```